Dinely Refuse Ireland

Hi There,

We are a biofuels company based in Ireland. We produce biodiesel from waste cooking oils from restaurants and biogas from food waste.

We are mainly a B2B company - essentially we take from collectors of these products and they aggregate for us.

We would like to start collections of our own for both waste cooking oil
and food waste from restaurants, hotels, hospitals and offices. We will pay for the waste oil (a main focus) and charge competitive rates for the food waste - all will go to renewable solutions.

Can you design a logo for this business? And then also can you provide a leaflet outline so we can send to businesses/ post on social media. Emphasis should be on the circular model of our business.
Updates

Target Market(s)

Restaurants and Businesses

Industry/Entity Type

Waste Collection

Colors
0094D4
00A9DD
6FCCEA
C7EBF8
E9F6FB
00AB8E
00BBA5
67D7C9
C6EFE9
E9F9F6
59FF00
82FF00
B8FF75
E3FFCB
F4FFEA
FFF300
FFF600
FEFA6F
FFFEC7
FFFEE8

Requirements
Nice to have
• Renewable Ideas, Circular Nature

```html
<!DOCTYPE html>
<html lang="en">
<head>
<meta charset="utf-8">
<title>Turn Your Waste Into Renewable Energy – Leaflet</title>
<link rel="stylesheet" href="https://fonts.googleapis.com/css2?family=Anton&family=Chewy&family=Playfair+Display:wght@800;900&family=Poppins:wght@500;600;700&display=swap">
<style>
  :root {
    --page-bg: #ececec;
    --green-light: #8fd46a;
    --green-mid: #4fb32f;
    --green-deep: #2a8a1e;
    --green-dark: #1d6516;
    --yellow: #fde12d;
    --yellow-warm: #f7c82e;
    --cream: #f4efe4;
    --ink: #111111;
    --white: #ffffff;
  }
  * { box-sizing: border-box; margin: 0; padding: 0; }
  html, body { width: 1200px; height: 1200px; overflow: hidden; }
  body { background: var(--page-bg); position: relative; font-family: "Poppins", sans-serif; }

  .leaflet {
    position: absolute; left: 190px; top: 20px;
    width: 820px; height: 1160px;
    background: var(--cream); overflow: hidden;
    box-shadow: 0 20px 40px rgba(0,0,0,.18);
  }
  .leaflet-shapes { position: absolute; inset: 0; }
  .abs { position: absolute; }

  .headline {
    left: 20px; top: 40px; width: 780px; text-align: center; white-space: nowrap;
    font-family: "Playfair Display", serif; font-weight: 900;
    font-size: 60px; line-height: 1; color: var(--ink);
  }
  .subhead {
    left: 20px; top: 112px; width: 780px; text-align: center; white-space: nowrap;
    font-family: "Playfair Display", serif; font-weight: 800;
    font-size: 34px; line-height: 1.1; color: var(--white);
    text-shadow: 2px 2px 0 var(--green-dark);
  }

  .tag-small { font-weight: 700; font-size: 20px; color: var(--ink); line-height: 1; }
  .tag-big {
    font-family: "Anton", sans-serif; font-size: 38px; line-height: 1.05;
    color: var(--yellow); text-shadow: 2px 2px 0 var(--green-dark);
  }
  .waste-oil-tag { left: 50px; top: 196px; }
  .waste-oil-tag .tag-small { padding-left: 30px; }
  .food-oil-tag { left: 590px; top: 440px; text-align: right; }
  .food-oil-tag .tag-small { padding-right: 20px; }

  .placeholder { position: absolute; border-radius: 14px; }
  .ph-barrel { left: 40px; top: 270px; width: 170px; height: 120px;
    background: linear-gradient(135deg, #2c2c2c, #d8c23a); border-radius: 40% 20% 50% 30%; }
  .ph-bottle { left: 660px; top: 300px; width: 90px; height: 130px;
    background: linear-gradient(180deg, #f2d23c, #9bbf2a); border-radius: 30px 30px 20px 20px; }
  .ph-globe { left: 690px; top: 520px; width: 96px; height: 96px;
    background: radial-gradient(circle, #b9e39b, #4fa63a); border-radius: 50%; }
  .ph-jerrycan { left: 40px; top: 530px; width: 104px; height: 104px; border-radius: 50%;
    background: radial-gradient(circle, #9fe07a 40%, #1a5fb0 42%, #1a5fb0 48%, var(--yellow) 50%); }
  .ph-energy { left: 610px; top: 636px; width: 84px; height: 84px; border-radius: 50%;
    background: radial-gradient(circle, #2e3f4a 58%, var(--yellow) 60%); }
  .ph-station { left: 30px; top: 915px; width: 400px; height: 215px;
    background: linear-gradient(180deg, #7dbb4a, #2f6e22 70%, #6b6b6b); border-radius: 20px; }
  .badge-clean { left: 360px; top: 610px; width: 72px; height: 72px; border-radius: 50%;
    background: var(--green-deep); border: 2px solid var(--green-light); }

  .pill {
    position: absolute; background: var(--yellow); border-radius: 30px;
    padding: 10px 26px; box-shadow: 0 3px 0 var(--green-dark); white-space: nowrap;
  }
  .pill-small { font-weight: 700; font-size: 20px; color: var(--ink); line-height: 1.1; }
  .pill-big { font-family: "Anton", sans-serif; font-size: 32px; color: var(--green-dark); line-height: 1.1; }
  .pill-uco { left: 40px; top: 656px; }
  .pill-food { left: 480px; top: 736px; text-align: center; }

  .bullets { position: absolute; list-style: disc; padding-left: 18px;
    font-weight: 600; font-size: 15px; line-height: 1.35; color: var(--ink); }
  .bullets-uco { left: 50px; top: 772px; width: 440px; }
  .bullets-food { left: 470px; top: 836px; width: 330px; font-size: 14px; }
  .bullets-why { left: 480px; top: 1042px; width: 320px; color: var(--yellow); font-size: 14px; }

  .why-bubble { left: 456px; top: 944px; width: 150px; height: 92px; }
  .why-text { left: 456px; top: 950px; width: 150px; text-align: center;
    font-family: "Chewy", cursive; font-size: 46px; line-height: 1.2; color: var(--yellow); }
</style>
</head>
<body>
<article class="leaflet">
  <svg class="leaflet-shapes" width="820" height="1160" viewBox="0 0 820 1160" aria-hidden="true">
    <defs>
      <linearGradient id="topGreen" x1="0" y1="0" x2="0" y2="1">
        <stop offset="0" stop-color="#b4e495"/>
        <stop offset="0.5" stop-color="#5fbf35"/>
        <stop offset="1" stop-color="#3a9b25"/>
      </linearGradient>
      <linearGradient id="bottomGreen" x1="0" y1="0" x2="1" y2="1">
        <stop offset="0" stop-color="#3fa12a"/>
        <stop offset="1" stop-color="#14520f"/>
      </linearGradient>
    </defs>
    <path d="M0 0 H820 V600 Q620 720 330 700 Q140 686 0 620 Z" fill="#1d6516"/>
    <path d="M0 0 H820 V574 Q620 692 330 674 Q140 662 0 598 Z" fill="url(#topGreen)"/>
    <path d="M0 930 Q220 860 460 905 Q640 940 820 880 V1160 H0 Z" fill="#f7c82e"/>
    <path d="M380 1160 Q450 1010 620 990 Q730 978 820 940 V1160 Z" fill="url(#bottomGreen)"/>
    <path d="M0 1090 Q200 1060 380 1160 H0 Z" fill="#9bbf2a"/>
    <g transform="translate(420 410)">
      <circle r="165" fill="none" stroke="#2a8a1e" stroke-width="24" stroke-dasharray="240 106"/>
      <circle r="128" fill="#fdc82e"/>
      <g fill="none" stroke="#ffffff" stroke-width="22" stroke-linecap="round">
        <path d="M-46 -38 A60 60 0 0 1 46 -38"/>
        <path d="M-46 -38 A60 60 0 0 1 46 -38" transform="rotate(120)"/>
        <path d="M-46 -38 A60 60 0 0 1 46 -38" transform="rotate(240)"/>
      </g>
      <g fill="#ffffff">
        <polygon points="40,-62 76,-30 30,-16"/>
        <polygon points="40,-62 76,-30 30,-16" transform="rotate(120)"/>
        <polygon points="40,-62 76,-30 30,-16" transform="rotate(240)"/>
      </g>
    </g>
  </svg>

  <h1 class="abs headline">TURN YOUR WASTE</h1>
  <p class="abs subhead">INTO RENEWABLE ENERGY!</p>

  <div class="abs waste-oil-tag">
    <div class="tag-small">WASTE OIL</div>
    <div class="tag-big">COLLECTION</div>
  </div>
  <div class="placeholder ph-barrel" role="img" aria-label="Illustration of a tipped barrel pouring golden waste oil"></div>

  <div class="placeholder ph-bottle" role="img" aria-label="Illustration of a bottle of cooking oil with olives"></div>
  <div class="abs food-oil-tag">
    <div class="tag-small">FOOD OIL</div>
    <div class="tag-big">COLLECTION</div>
  </div>

  <div class="placeholder ph-globe" role="img" aria-label="Illustration of a green globe with leaves"></div>
  <div class="placeholder ph-jerrycan" role="img" aria-label="Icon of a green fuel can with a leaf"></div>
  <div class="abs badge-clean" aria-hidden="true"></div>
  <div class="placeholder ph-energy" role="img" aria-label="Icon of a plug surrounded by leaves"></div>

  <div class="pill pill-uco">
    <div class="pill-small">Used Cooking Oil</div>
    <div class="pill-big">(UCO) COLLECTION</div>
  </div>
  <ul class="bullets bullets-uco">
    <li>Competitive prices for UCO with collection within 48 hours.</li>
    <li>Servicing restaurants, bars, hotels, event venues, hospitals, and canteens.</li>
    <li>Your waste is converted into clean, green biodiesel.</li>
  </ul>

  <div class="pill pill-food">
    <div class="pill-small">FOOD</div>
    <div class="pill-big">WASTE COLLECTION</div>
  </div>
  <ul class="bullets bullets-food">
    <li>Starting at €10 per lift for a 240L bin.</li>
    <li>Monthly bin cleaning included.</li>
    <li>Food waste is converted into biomethane at our Meath facility.</li>
  </ul>

  <div class="placeholder ph-station" role="img" aria-label="Illustration of a green renewable fuel station with trees and a car"></div>

  <svg class="abs why-bubble" viewBox="0 0 150 92" aria-hidden="true">
    <path d="M10 6 H140 Q148 6 148 14 V66 Q148 74 140 74 H60 L40 90 L44 74 H10 Q2 74 2 66 V14 Q2 6 10 6 Z" fill="#1d6516"/>
  </svg>
  <div class="abs why-text">Why?</div>
  <ul class="bullets bullets-why">
    <li>Monthly bin cleaning included!</li>
    <li>All food waste is converted into biomethane at our anaerobic digestion facility in Meath.</li>
  </ul>
</article>
</body>
</html>
```